Web site for small printshop

I am looking for a website for small printshop in Iceland, mainly serving university students and artist.

We print posters, flyers, business cards and more.

In addition to our current website, I would like to include design tool, (fx. www.quarlitune.example, www.dravonpix.example or something similar) jobs upload, shopping chart.
Updates

Great work, I am really amazed of the quality of work i am seeing here.

Really way beyond my expectation

GOOD JOB - all of you ! 

Hi all.

The designs submitted have been great, way better than expected.
I really did not expect this level of quality.

Some have been asking me for feedback on their designs, and I will try 
to send some feedback here, without spoiling your creativity.

Likes:
- when the colors of my logo is used in menus, buttons etc.
- simple, not to crowded look.

Dislikes.
- Dark and heavy design
- Lot of text and buttons (crowded look)

Extra info.
- top line (before menus) will contain: Tel - email - language
- menu line will have 5 categories: Home - service - submission of works - FAQ - about us
- 3 large buttons:  Job submit - Job design - ask for offer

LOVE YOUR WORK - great designs so far :)

Target Market(s)

University Students, Artists. Age group 20-30

Industry/Entity Type

University

Requirements
Must have
• The website must be easy to use, clean looking.

```html
<!DOCTYPE html>
<html lang="en">
<head>
<meta charset="utf-8">
<title>Fjalla Press – Printshop</title>
<link rel="stylesheet" href="https://fonts.googleapis.com/css2?family=Open+Sans:wght@400;600;700&display=swap">
<style>
  :root {
    --red: #e5262b;
    --ink: #333333;
    --text: #444444;
    --muted: #777777;
    --page: #f7f7f7;
    --band: #efefef;
    --footer: #2b2b2b;
    --footer-text: #bbbbbb;
    --yellow: #f3d21c;
    --green: #1c6b22;
    --circle: #333333;
  }
  * { box-sizing: border-box; margin: 0; padding: 0; }
  html, body { width: 782px; height: 1200px; overflow: hidden; }
  body {
    position: relative;
    font-family: "Open Sans", Arial, sans-serif;
    background: var(--page);
    color: var(--text);
  }
  .abs { position: absolute; }

  /* Header */
  .brand { left: 91px; top: 25px; font-size: 18px; font-weight: 600; color: var(--ink); }
  .main-nav { left: 326px; top: 27px; display: flex; align-items: center; }
  .main-nav a { text-decoration: none; font-size: 12px; font-weight: 600; color: var(--ink); margin-right: 17px; }
  .main-nav a.is-active {
    background: var(--red); color: #fff; width: 64px; height: 21px; line-height: 21px;
    text-align: center; margin-right: 11px; border-radius: 1px;
  }
  .search { left: 578px; top: 28px; width: 125px; height: 19px; background: #fff; border: 1px solid #cfcfcf;
    font-size: 9px; color: #999; font-style: italic; padding: 3px 8px; }
  .search svg { position: absolute; right: 5px; top: 4px; }

  /* Hero */
  .hero-wing { top: 309px; width: 0; height: 0; border-top: 22px solid #cfcfcf; }
  .hero-wing.left { left: 70px; border-left: 8px solid transparent; }
  .hero-wing.right { left: 704px; border-right: 8px solid transparent; }
  .hero {
    left: 78px; top: 70px; width: 626px; height: 261px; overflow: hidden;
    background: linear-gradient(100deg, #7a2a0c 0%, #a5410f 30%, #8c3a14 48%, #4a3a4e 62%, #6a5a6e 80%, #8a6a4a 100%);
  }
  .hero-copy { left: 27px; top: 64px; }
  .hero-copy .kicker { font-size: 21px; color: var(--yellow); line-height: 1.1; }
  .hero-copy h1 { font-size: 31px; font-weight: 400; color: var(--yellow); line-height: 1.2; }
  .hero-copy p { font-size: 11px; color: #fff; line-height: 15px; width: 220px; margin-top: 10px; }
  .btn-learn { left: 27px; top: 176px; width: 101px; height: 28px; background: var(--green);
    color: #fff; font-size: 12.5px; font-weight: 600; line-height: 28px; padding-left: 9px; }
  .btn-learn svg { position: absolute; right: 11px; top: 10px; }
  .hero-arrows { left: 543px; top: 225px; width: 83px; height: 36px; background: rgba(230,215,200,0.75); }
  .hero-arrows svg { position: absolute; top: 9px; }

  /* Services */
  .section-title { left: 0; width: 782px; top: 356px; text-align: center; font-size: 24px; font-weight: 600; color: var(--ink); }
  .section-title span { color: var(--red); }
  .title-rule { left: 78px; top: 393px; width: 626px; height: 1px; background: #dddddd; }
  .title-dot { left: 387px; top: 390px; width: 7px; height: 7px; border-radius: 50%; background: #cccccc; }
  .intro { left: 90px; top: 406px; width: 602px; text-align: center; font-size: 10px; line-height: 12px; color: var(--muted); }
  .service { top: 448px; width: 140px; text-align: center; }
  .service-icon { width: 85px; height: 85px; border-radius: 50%; background: var(--circle); margin: 0 auto;
    display: flex; align-items: center; justify-content: center; }
  .service.is-active .service-icon { background: var(--red); }
  .service-shadow { width: 60px; height: 5px; margin: 7px auto 0; border-radius: 50%;
    background: radial-gradient(ellipse, rgba(0,0,0,0.18), transparent 70%); }
  .service h3 { font-size: 12px; font-weight: 400; color: var(--ink); margin-top: 6px; }
  .service.is-active h3 { color: var(--red); }
  .service p { font-size: 9px; line-height: 10.5px; color: var(--text); width: 106px; margin: 4px auto 0; }

  /* Feature band */
  .band { left: 0; top: 636px; width: 782px; height: 534px; background: var(--band); }
  .feature h2 { font-size: 16.5px; font-weight: 400; color: var(--ink); white-space: nowrap; }
  .feature h2 span { color: var(--red); }
  .feature p { font-size: 9.6px; line-height: 13px; color: var(--text); margin-top: 10px; }
  .feature-media { box-shadow: 0 8px 8px -6px rgba(0,0,0,0.25); }

  /* Footer */
  .site-footer { left: 0; top: 1170px; width: 782px; height: 30px; background: var(--footer);
    font-size: 8.6px; color: var(--footer-text); }
  .footer-links { position: absolute; left: 77px; top: 9px; }
  .footer-copy { position: absolute; right: 78px; top: 9px; }
</style>
</head>
<body>

<header>
  <div class="abs brand">Fjalla Press</div>
  <nav class="abs main-nav">
    <a href="#" class="is-active">Home</a>
    <a href="#">Features</a>
    <a href="#">Demo</a>
    <a href="#">Contact</a>
  </nav>
  <div class="abs search">Search....
    <svg width="9" height="9" viewBox="0 0 9 9"><circle cx="3.6" cy="3.6" r="2.6" fill="none" stroke="#e5262b" stroke-width="1.4"/><line x1="5.5" y1="5.5" x2="8.2" y2="8.2" stroke="#e5262b" stroke-width="1.6"/></svg>
  </div>
</header>

<div class="abs hero-wing left"></div>
<div class="abs hero-wing right"></div>
<section class="abs hero" role="img" aria-label="Photo of printed mugs and colourful coasters on a wooden table">
  <div class="abs hero-copy">
    <div class="kicker">Welcome to</div>
    <h1>Fjalla Press</h1>
    <p>Lorem Ipsum is simply dummy text of the printing and typesetting industry.</p>
  </div>
  <a class="abs btn-learn">Learn More
    <svg width="6" height="9" viewBox="0 0 6 9"><polyline points="1,1 5,4.5 1,8" fill="none" stroke="#fff" stroke-width="1.4"/></svg>
  </a>
  <div class="abs hero-arrows">
    <svg style="left:18px" width="12" height="20" viewBox="0 0 12 20"><polyline points="11,1 1,10 11,19" fill="none" stroke="#333" stroke-width="1.6"/></svg>
    <svg style="left:55px" width="12" height="20" viewBox="0 0 12 20"><polyline points="1,1 11,10 1,19" fill="none" stroke="#333" stroke-width="1.6"/></svg>
  </div>
</section>

<section>
  <h2 class="abs section-title"><span>OUR</span> SERVICES</h2>
  <div class="abs title-rule"></div>
  <div class="abs title-dot"></div>
  <p class="abs intro">Lorem Ipsum is simply dummy text of the printing and typesetting industry. Lorem Ipsum has been the industry's standard dummy text ever since the 1500s, when an unknown printer took a galley of type and scrambled .</p>

  <div class="abs service" style="left:86px">
    <div class="service-icon">
      <svg width="40" height="36" viewBox="0 0 40 36" fill="none" stroke="#fff" stroke-width="2">
        <rect x="3" y="9" width="32" height="24" rx="2"/><rect x="9" y="14" width="20" height="14"/>
        <line x1="18" y1="24" x2="33" y2="3"/><line x1="31" y1="2" x2="35" y2="5"/>
      </svg>
    </div>
    <div class="service-shadow"></div>
    <h3>Design Templates</h3>
    <p>Lorem Ipsum is simply dummy text of the printing industry.</p>
  </div>

  <div class="abs service" style="left:243px">
    <div class="service-icon">
      <svg width="36" height="36" viewBox="0 0 36 36" stroke="#fff" stroke-width="3.2" stroke-linecap="round">
        <line x1="18" y1="3" x2="18" y2="9"/><line x1="18" y1="27" x2="18" y2="33"/>
        <line x1="3" y1="18" x2="9" y2="18"/><line x1="27" y1="18" x2="33" y2="18"/>
        <line x1="7.4" y1="7.4" x2="11.6" y2="11.6"/><line x1="24.4" y1="24.4" x2="28.6" y2="28.6"/>
        <line x1="7.4" y1="28.6" x2="11.6" y2="24.4"/><line x1="24.4" y1="11.6" x2="28.6" y2="7.4"/>
      </svg>
    </div>
    <div class="service-shadow"></div>
    <h3>Save and Load Designs</h3>
    <p>Lorem Ipsum is simply dummy text of the printing industry.</p>
  </div>

  <div class="abs service is-active" style="left:399px">
    <div class="service-icon">
      <svg width="36" height="28" viewBox="0 0 36 28"><polyline points="4,14 14,23 32,5" fill="none" stroke="#fff" stroke-width="6"/></svg>
    </div>
    <div class="service-shadow"></div>
    <h3>Ready to Deploy</h3>
    <p>Lorem Ipsum is simply dummy text of the printing industry.</p>
  </div>

  <div class="abs service" style="left:556px">
    <div class="service-icon">
      <svg width="38" height="30" viewBox="0 0 38 30" fill="none" stroke="#fff" stroke-width="2" stroke-linejoin="round">
        <path d="M2 10 L10 4 L20 8 L28 4 L36 10"/>
        <path d="M8 12 L18 24 Q21 27 23 24 L30 14"/>
        <path d="M14 14 L22 22 M18 12 L25 19"/>
      </svg>
    </div>
    <div class="service-shadow"></div>
    <h3>Best Deal</h3>
    <p>Lorem Ipsum is simply dummy text of the printing industry.</p>
  </div>
</section>

<div class="abs band"></div>

<article class="abs feature" style="left:93px; top:688px; width:322px">
  <h2><span>Fully</span> Customizable</h2>
  <p>Lorem Ipsum is simply dummy text of the printing and typesetting industry. Lorem Ipsum has been the industry's standard dummy text ever since the 1500s, when an unknown printer took a galley of type and scrambled it to make a type specimen book.</p>
</article>
<div class="abs feature-media" role="img" aria-label="Photo of an orange flower on a desk with pens and prints"
     style="left:470px; top:668px; width:219px; height:140px; background: radial-gradient(circle at 50% 55%, #f6b21a 0%, #e89412 35%, #6a4a32 75%, #4a3a2e 100%);"></div>

<div class="abs feature-media" role="img" aria-label="Illustration of devices sending print jobs through the cloud to printers"
     style="left:93px; top:828px; width:218px; height:139px; background: linear-gradient(160deg, #ffffff 0%, #eef3f6 50%, #e2e8ea 100%);"></div>
<article class="abs feature" style="left:353px; top:846px; width:340px">
  <h2><span>Extensibile</span> via Modules</h2>
  <p style="margin-top:6px">Development of customized, remote access and data collection/analysis solutions for commercial and industrial equipment manufacturers. The founders of Brightfield Systems have been building these specialized applications since the 1990's. Let us show you how you too can benefit from incorporating remote access technology into your product.</p>
</article>

<article class="abs feature" style="left:92px; top:1024px; width:322px">
  <h2><span>Generate Full Vector</span> PDF or High res JPEGs</h2>
  <p style="margin-top:12px">Lorem Ipsum is simply dummy text of the printing and typesetting industry. Lorem Ipsum has been the industry's standard dummy text ever since the 1500s, when an unknown printer took a galley of type and scrambled it to make a type specimen book.</p>
</article>
<div class="abs feature-media" role="img" aria-label="Diagram of a PDF printer, server and client computers linked over a network"
     style="left:470px; top:987px; width:219px; height:139px; background: linear-gradient(160deg, #ffffff 0%, #f1f3f5 60%, #e6e9ec 100%);"></div>

<footer class="abs site-footer">
  <div class="footer-links">Home &nbsp;|&nbsp; Demo &nbsp;|&nbsp; Features &nbsp;|&nbsp; Contact &nbsp;|&nbsp; Terms of Use &nbsp;|&nbsp; Privacy Policy</div>
  <div class="footer-copy">Copyright Fjalla Press® 2003-13. All rights reserved</div>
</footer>

</body>
</html>
```